Designing HTML Email Creative

Hi There,
The goal of this project is to design an HTML Email Creative.
Target Market: Minority Women 25 - 45. Low Household incomes. Stay at home moms. Middle America
Subject of Email Campaign: Top 5 Reasons To Go Back to College
The goal is to make the users Buy the top 5 reasons to go back to school and then Get Matched to Online & Local Colleges.
Call to action: Get Matched to Online & Local Colleges
You can add two buttons, one above the reasons and one below. The text in the button should be: Get Matched to Online & Local Colleges Now!
Your goal is to make the call to action in the email pop out so that users know very easily where to click to visit our site.
Please find attached the copy that is to be used in the creative.
Also, the information needs to be sourced so you can create very small links in the bottom of the email.
Also, we just need the psd file for this. Does not need to be coded.
Also, you can find some successful email creative attached so you have an idea.
Updates
Please note that we have updated the word doc with the correct content.
Target Market(s)
Women 25 - 50 - Low Household Incomes - Middle America
Industry/Entity Type
School
Look and feel

```html
<!DOCTYPE html>
<html lang="en">
<head>
<meta charset="utf-8">
<title>Top Reasons to Go Back to College</title>
<link rel="stylesheet" href="https://fonts.googleapis.com/css2?family=Arimo:wght@400;700&family=Noto+Serif:wght@400;700&family=Cinzel:wght@400;700&display=swap">
<style>
  :root {
    --page: #ffffff;
    --card-border: #d9dde2;
    --header-deep: #0b3fc4;
    --header-mid: #1e63e6;
    --header-light: #cfe3fb;
    --title-white: #ffffff;
    --title-gold: #f1b419;
    --title-gold-dark: #c98a0a;
    --heading-blue: #1f4fbf;
    --subtitle-grey: #444a52;
    --reason-red: #d9261c;
    --body-text: #2e2e2e;
    --button-top: #ff6a2a;
    --button-bottom: #d91f0a;
    --footer-band: #e9ecef;
    --footer-text: #3c4148;
    --link-blue: #1646c8;
    --cite-text: #333333;
  }
  * { margin: 0; padding: 0; box-sizing: border-box; }
  html, body { width: 1200px; height: 2880px; overflow: hidden; background: var(--page); }
  body { position: relative; font-family: "Arimo", Arial, sans-serif; color: var(--body-text); }

  .email-card {
    position: absolute; left: 27px; top: 15px; width: 1143px; height: 2140px;
    border: 2px solid var(--card-border); background: var(--page);
  }

  .hero {
    position: absolute; left: 0; top: 0; width: 100%; height: 490px; overflow: hidden;
    background:
      radial-gradient(ellipse 70% 60% at 20% 110%, var(--header-light) 0%, rgba(207,227,251,0) 70%),
      radial-gradient(ellipse 60% 50% at 85% -10%, #5a9af5 0%, rgba(90,154,245,0) 70%),
      linear-gradient(160deg, var(--header-mid) 0%, var(--header-deep) 55%, #2a7ae8 100%);
  }
  .hero__illustration {
    position: absolute; left: 140px; top: 70px; width: 450px; height: 400px;
    border-radius: 40px;
    background: radial-gradient(ellipse at 45% 40%, #3b3f47 0%, #22252b 45%, rgba(230,230,230,0.85) 75%, rgba(255,255,255,0) 100%);
  }
  .hero__title {
    position: absolute; left: 560px; top: 130px; width: 560px; text-align: center;
    font-family: "Cinzel", "Noto Serif", serif; color: var(--title-white);
  }
  .hero__line-top { font-size: 54px; letter-spacing: 3px; line-height: 62px; }
  .hero__line-mid { font-size: 40px; letter-spacing: 3px; line-height: 56px; }
  .hero__line-main {
    font-size: 104px; font-weight: 700; line-height: 110px; letter-spacing: 2px;
    color: var(--title-gold);
    background: linear-gradient(180deg, #ffd65a 0%, var(--title-gold) 50%, var(--title-gold-dark) 100%);
    -webkit-background-clip: text; background-clip: text; -webkit-text-fill-color: transparent;
  }

  .intro__heading {
    position: absolute; left: 55px; top: 550px;
    font-family: "Noto Serif", serif; font-size: 54px; font-weight: 400; color: var(--heading-blue);
  }
  .intro__text {
    position: absolute; left: 57px; top: 630px; width: 620px;
    font-family: "Noto Serif", serif; font-size: 29px; line-height: 42px; color: var(--subtitle-grey);
  }

  .cta-button {
    position: absolute; display: flex; align-items: center; justify-content: center; text-align: center;
    width: 375px; height: 104px; border-radius: 16px;
    background: linear-gradient(180deg, var(--button-top) 0%, var(--button-bottom) 100%);
    box-shadow: 0 4px 8px rgba(0,0,0,0.28), inset 0 2px 0 rgba(255,255,255,0.35);
    color: #ffffff; font-family: "Arimo", Arial, sans-serif; font-weight: 700;
    font-size: 30px; line-height: 38px; text-decoration: none;
  }
  .cta-button--top { left: 703px; top: 600px; }
  .cta-button--bottom { left: 378px; top: 1915px; }

  .reason { position: absolute; left: 63px; width: 1020px; top: var(--y); }
  .reason__title { font-size: 25px; line-height: 32px; color: var(--reason-red); font-weight: 400; }
  .reason__text { font-size: 20.5px; line-height: 32px; margin-top: 8px; }
  .reason__plain { font-size: 20.5px; line-height: 32px; }

  .footer-band {
    position: absolute; left: 0; bottom: 0; width: 100%; height: 78px;
    background: linear-gradient(180deg, #f6f7f8 0%, var(--footer-band) 100%);
    display: flex; align-items: center; justify-content: center;
    font-size: 25px; color: var(--footer-text);
  }
  .footer-band a { color: var(--link-blue); font-weight: 700; text-decoration: none; margin: 0 8px; }

  .sources { position: absolute; left: 60px; top: 2195px; width: 1080px; font-size: 15px; line-height: 22px; color: var(--cite-text); }
  .sources__item { margin-bottom: 7px; }
  .sources__link { color: var(--link-blue); }
</style>
</head>
<body>
  <main class="email-card">
    <header class="hero">
      <div class="hero__illustration" role="img" aria-label="Graduation cap with gold tassel resting on a rolled diploma tied with a red ribbon"></div>
      <h1 class="hero__title">
        <div class="hero__line-top">TOP REASONS</div>
        <div class="hero__line-mid">TO GO BACK TO</div>
        <div class="hero__line-main">COLLEGE</div>
      </h1>
    </header>

    <h2 class="intro__heading">Empower Yourself!</h2>
    <p class="intro__text">Education frees you financially and boosts your self-esteem and self-confidence.</p>
    <a class="cta-button cta-button--top" href="#">Get Matched to<br>Online &amp; Local Colleges</a>

    <section class="reasons">
      <div class="reason" style="--y:780px">
        <h3 class="reason__title">1. Education pays – Make Twice As Much</h3>
        <p class="reason__text">College grads earn nearly twice as much as those with only high school diplomas. Median weekly salary with high school diploma, $652.&nbsp; Median weekly salary with Bachelor's degree $1,066.</p>
      </div>
      <div class="reason" style="--y:905px">
        <h3 class="reason__title">2.&nbsp; Government Grants – Federal Access Grants</h3>
        <p class="reason__text">College is more affordable than you think.&nbsp; Federal Access Grants of up to $5,550 are available to qualifying students.&nbsp; Grants are free money, which does not have to be paid back.&nbsp; Other Federal and state grants are also available, as are low cost government loans and countless scholarships.</p>
      </div>
      <div class="reason" style="--y:1072px">
        <p class="reason__plain">3. Be a role model. Children are inspired to take education seriously when they see you studying.</p>
      </div>
      <div class="reason" style="--y:1120px">
        <p class="reason__plain">4. Invest in yourself and your family's future.&nbsp; Education boosts your communication skills as well as your employability.&nbsp; Better communication= more satisfying relationships.</p>
      </div>
      <div class="reason" style="--y:1216px">
        <h3 class="reason__title">5. Lower Unemployment Rates for College Grads.</h3>
        <p class="reason__text">High school graduates 8.3% unemployed, college graduates 4.5 % unemployed.</p>
      </div>
      <div class="reason" style="--y:1321px">
        <h3 class="reason__title">6. Make $1 Million More in Lifetime – Retirement Security</h3>
        <p class="reason__text">On average, those with a bachelor's degree earn a $1 million more in their lifetime than those with a high school diploma.</p>
      </div>
      <div class="reason" style="--y:1440px">
        <p class="reason__plain">7.&nbsp; Job satisfaction.&nbsp; 60% of college graduates report being satisfied with their job compared to 50% of high school graduates .</p>
      </div>
      <div class="reason" style="--y:1531px">
        <p class="reason__plain">8.&nbsp; Boost your brain health.&nbsp; Studies show learning improves the memory and keeps the brain strong.</p>
      </div>
      <div class="reason" style="--y:1579px">
        <p class="reason__plain">9.&nbsp; Be your own boss.&nbsp; In 2002, a National Survey Office study found that 64 % of business owners surveyed had a least some college credit, while 23 % had bachelor's degrees.</p>
      </div>
      <div class="reason" style="--y:1648px">
        <p class="reason__plain">10.&nbsp; Be more employable.&nbsp; Of the 2 million plus job added during the recent U.S. economic recovery, the majorities were for college graduates.</p>
      </div>
      <div class="reason" style="--y:1728px">
        <p class="reason__plain">11.&nbsp; Advance your career. College graduates can continue to improve their employability and lifetime earnings by taking advanced degrees.&nbsp; Median weekly salary with a Master's degree $1,300; Median weekly salary with a professional degree $1,735.</p>
      </div>
      <div class="reason" style="--y:1847px">
        <p class="reason__plain">12.&nbsp; A sense of accomplishment—a priceless, permanent possession.</p>
      </div>
    </section>

    <a class="cta-button cta-button--bottom" href="#">Get Matched to<br>Online &amp; Local Colleges</a>

    <footer class="footer-band">
      You with a college degree—oh the places you will go.<a href="#">Click here</a>to explore the possibilities.
    </footer>
  </main>

  <section class="sources">
    <p class="sources__item">"Education Pays," National Labor Data Office, January 28&nbsp; 2013.&nbsp; Accessed April 21, 2013 <span class="sources__link">&lt;www.labordata.example.gov/emp/ep_chart_001.htm&gt;</span></p>
    <p class="sources__item">"Access Grants" Student Aid Center--A Federal Education Office. Accessed April 21, 2013.<br><span class="sources__link">&lt;http://studentaid.example.gov/types/grants-scholarships/access&gt;</span></p>
    <p class="sources__item">"The Role of Parents"&nbsp; Family Learning Network. Accessed April 20, 2013.<br><span class="sources__link">&lt;www.familylearning.example.org/education/going-to-school/supporting-your-learner/role-of-parents&gt;</span></p>
    <p class="sources__item">Marlowe, Daniel. "A Liberal Arts Degree Is More Valuable Than Learning Any Trade" November 13, 2012.&nbsp; Accessed April 19, 2013.<br><span class="sources__link">&lt;www.bizweekly.example.com/sites/dmarlowe/2012/11/13/a-liberal-arts-degree-is-more-valuable-than-learning-any-trade/&gt;</span></p>
    <p class="sources__item">"Education Pays," National Labor Data Office, January 28&nbsp; 2013.&nbsp; Accessed April 21, 2013 <span class="sources__link">&lt;www.labordata.example.gov/emp/ep_chart_001.htm&gt;</span></p>
    <p class="sources__item">National Survey Office, October 2012. Accessed April 20, 2013. <span class="sources__link">&lt;www.survey.example.gov/prod/2012pubs/acsbr11-04.pdf&gt;</span></p>
    <p class="sources__item">Hartley, Joan. "Top 10 Benefits of a College Degree"&nbsp; Daily Ledger. Accessed April 20, 2013.<br><span class="sources__link">&lt;www.dailyledger.example.com/Business/2010/1028/Top-10-benefits-of-a-college-degree/Higher-job-satisfaction &gt;</span></p>
    <p class="sources__item">"Learning Helps Keep Brain Healthy" Westbrook State University, March 2, 2010.&nbsp; Accessed April 20, 2013.<br><span class="sources__link">&lt;http://news.westbrook.example.edu/2010/03/hr_gall_100302.php&gt;</span></p>
    <p class="sources__item">"2002 Survey of Business Owners: Summary of Findings"&nbsp; National Survey Office, 2002. Accessed April 20, 2013.<br><span class="sources__link">&lt;www.survey.example.gov/econ/sbo/02/cbosof.html&gt;</span></p>
    <p class="sources__item">Avery, Claire. "What is a College Education Worth?" Mind Matters Journal, August 16 2012.&nbsp; Accessed April 20, 2013.<br><span class="sources__link">&lt;www.mindmatters.example.com/blog/good-thinking/201208/what-s-college-education-worth&gt;</span></p>
    <p class="sources__item">"Education Pays," National Labor Data Office, January 28&nbsp; 2013.&nbsp; Accessed April 21, 2013 &lt;http://www.labordata.example.gov/emp/ep_chart_001.htm&gt;<br>&nbsp;Avery, Claire. "What is a College Education Worth?" Mind Matters Journal, August 16 2012.&nbsp; Accessed April 20, 2013.<br><span class="sources__link">&lt;www.mindmatters.example.com/blog/good-thinking/201208/what-s-college-education-worth&gt;</span></p>
  </section>
</body>
</html>
```